Small Local Computer Shop Website Needed

Im after a new website that goes with my brand logo.
We are a small all family run local computer repair company and would like to drive more business via the site.
I have added my old site and one that was in progress also a Facebook link to give you an idea.

I would like to be able to make it stand out more and be easy to navigate.
I am basically a small computer repair shop, we offer in store repairs and upgrades. We also do call outs to your home or business and we also sell laptops,pcs and peripherals.

We do sell Laptops and pcs and although i don't really want to sell directly from the web it would be nice to be able to show what we have on offer on our site, Roughly 20-30 items generally.

Current site
http://byte-vale.com

New Site
http://byte-vale.com/site/

Facebook
http://www.sociabook.com/pages/Byte-Vale/847315902264710

images and files are available.

Many Thanks
Hugo
Byte Vale

Target Market(s)

I cater for all ages!

Industry/Entity Type

It Company

Number of Pages Required

5+ page

Font styles to use
Sans Serif

Requirements
Must have
• Be nice to keep in theme with my Logo.
• Landing page.
• Contact page
• about us
• Laptops (Displaying products currently for sale in store) Generally 10-20 at a time
• Pcs (Displaying products currently for sale in store)
Nice to have
• i would like and easy way for the customers to navigate to my remote support site. ie.
• https://www.remotorhelp.com/
• Easy link to download there trial off shieldwarren antivirus.
• ie http://downloads.shieldwarren.com/partners/rskit/ShieldWarrenDownloader_bytevalekit.exe
• Link to our Repair tracker... When we check in a computer or laptop repair the Customers can see how there jobs progressing by clicking the link. ie http://byte-vale.com/shop/repairstatus/
• would be great if there was a fairly straight forward way to add/ remove pc's and laptops for sale on our site.
• Maybe check our facebook for ideas images etc..
• https://www.sociabook.com/Byte-vale-847315902264710/
Should not have
• The site i currently have i really dislike, so please dont copy that theme.
• Had a few designs with a white banner at the top with my logo.
• Sorry but have decided these are not what i want.
• a darker theme is def more in line with what im looking for.
• Thanks

```html
<!DOCTYPE html>
<html lang="en">
<head>
<meta charset="utf-8">
<title>Byte Vale – Computer Repair</title>
<link rel="stylesheet" href="https://fonts.googleapis.com/css2?family=Questrial&family=Roboto:ital,wght@0,400;0,500;0,700;1,700&display=swap">
<style>
  :root {
    --header-top: #0b2a36;
    --header-bottom: #1c6a86;
    --teal: #22799c;
    --heading-blue: #1a5f80;
    --muted: #8a8f94;
    --text: #333;
    --band-grey: #efefef;
    --footer: #1b1b1b;
    --white: #fff;
    --red: #e04656;
    --orange: #e9962f;
    --cyan: #3cb8d9;
    --navy: #154f8c;
  }
  * { box-sizing: border-box; margin: 0; padding: 0; }
  html, body { width: 904px; height: 1200px; overflow: hidden; }
  body { position: relative; font-family: "Roboto", sans-serif; color: var(--text); background: var(--white); }

  .site-header { position: absolute; left: 0; top: 0; width: 904px; height: 88px;
    background: linear-gradient(180deg, var(--header-top), var(--header-bottom)); }
  .brand { position: absolute; left: 62px; top: 22px; display: flex; align-items: center; gap: 10px;
    font-family: "Questrial", sans-serif; font-size: 30px; color: var(--white); }
  .brand-dot { width: 14px; height: 14px; border-radius: 50%; background: var(--white); }
  .top-contact { position: absolute; left: 443px; top: 19px; font-size: 11.5px; color: var(--white); }
  .social { position: absolute; left: 726px; top: 15px; display: flex; gap: 6px; }
  .social span { width: 18px; height: 18px; border: 1px solid rgba(255,255,255,.8); border-radius: 50%; }
  .main-nav { position: absolute; left: 330px; top: 57px; display: flex; font-size: 12.5px; color: var(--white); }
  .main-nav a { color: inherit; text-decoration: none; }
  .main-nav .sep { margin: 0 16px; }
  .main-nav .active { font-weight: 700; border-bottom: 1px solid var(--white); padding-bottom: 2px; }
  .search-btn { position: absolute; left: 814px; top: 52px; width: 24px; height: 24px; border-radius: 50%; background: var(--white); }

  .hero { position: absolute; left: 0; top: 88px; width: 904px; height: 317px; }
  .hero-photo { position: absolute; inset: 0;
    background: linear-gradient(100deg, #c9d1d6 0%, #9fa9b0 30%, #d8d6d0 55%, #7d6a5c 100%); }
  .hero-title { position: absolute; left: 450px; top: 115px; width: 308px; height: 44px; background: var(--teal);
    font-family: "Questrial", sans-serif; font-weight: 400; font-size: 31px; color: var(--white); text-align: center; line-height: 44px; letter-spacing: .5px; }
  .hero-sub { position: absolute; left: 450px; top: 182px; width: 356px; font-size: 13px; font-weight: 700; font-style: italic;
    color: var(--white); line-height: 19px; letter-spacing: .9px; }

  .welcome-band { position: absolute; left: 0; top: 405px; width: 904px; height: 56px; background: var(--teal); color: var(--white); }
  .welcome-band .lead { position: absolute; left: 99px; top: 17px; font-size: 18px; font-weight: 500; letter-spacing: .6px; }
  .welcome-band .call { position: absolute; left: 445px; top: 14px; font-size: 22px; font-weight: 700; letter-spacing: 1px; }

  .services { position: absolute; left: 0; top: 461px; width: 904px; height: 342px;
    background: linear-gradient(160deg, #e9f3f8 0%, #ffffff 45%, #e4f0f6 100%); }
  .section-title { position: absolute; left: 0; width: 904px; top: 42px; text-align: center;
    font-size: 17px; font-weight: 500; letter-spacing: 1.5px; color: var(--heading-blue); }
  .section-sub { position: absolute; left: 0; width: 904px; top: 65px; text-align: center; font-size: 9.5px; color: var(--muted); }
  .section-rule { position: absolute; left: 312px; top: 84px; width: 280px; height: 1px; background: #c9d6dd; }
  .service { position: absolute; top: 118px; width: 200px; text-align: center; }
  .service-ring { width: 110px; height: 110px; margin: 0 auto; border-radius: 50%; border: 2px solid; padding: 5px; }
  .service-disc { width: 100%; height: 100%; border-radius: 50%; display: flex; align-items: center; justify-content: center; }
  .service h3 { margin-top: 18px; font-size: 12.5px; font-weight: 500; letter-spacing: 1.2px; }
  .service p { margin-top: 4px; font-size: 10px; line-height: 13px; color: var(--muted); padding: 0 12px; }
  .svc-red { left: 40px; } .svc-red .service-ring { border-color: var(--red); } .svc-red .service-disc { background: var(--red); } .svc-red h3 { color: var(--red); }
  .svc-orange { left: 239px; } .svc-orange .service-ring { border-color: var(--orange); } .svc-orange .service-disc { background: var(--orange); } .svc-orange h3 { color: var(--orange); }
  .svc-cyan { left: 446px; } .svc-cyan .service-ring { border-color: var(--cyan); } .svc-cyan .service-disc { background: var(--cyan); } .svc-cyan h3 { color: var(--cyan); }
  .svc-navy { left: 647px; } .svc-navy .service-ring { border-color: var(--navy); } .svc-navy .service-disc { background: var(--navy); } .svc-navy h3 { color: var(--navy); }

  .report-band { position: absolute; left: 0; top: 803px; width: 904px; height: 72px; background: var(--band-grey); }
  .report-band h2 { position: absolute; left: 62px; top: 12px; font-size: 18px; font-weight: 500; letter-spacing: 1.5px; color: var(--heading-blue); }
  .report-band p { position: absolute; left: 62px; top: 36px; width: 428px; font-size: 9px; line-height: 13px; color: #222; }
  .report-btn { position: absolute; left: 590px; top: 22px; width: 223px; height: 32px; border-radius: 6px; background: var(--teal);
    color: var(--white); font-size: 11px; font-weight: 700; letter-spacing: 1px; text-align: center; line-height: 32px; }

  .about { position: absolute; left: 0; top: 875px; width: 904px; height: 235px;
    background: linear-gradient(200deg, #dfeef6 0%, #ffffff 50%, #eaf4f9 100%); }
  .about h2 { position: absolute; left: 84px; top: 34px; font-size: 18px; font-weight: 500; letter-spacing: .8px; color: var(--heading-blue); }
  .about p { position: absolute; left: 84px; top: 60px; width: 370px; font-size: 10.5px; line-height: 22px; letter-spacing: .5px; color: #333; text-align: justify; }
  .about-photo { position: absolute; left: 513px; top: 40px; width: 303px; height: 160px; border-radius: 8px;
    background: linear-gradient(180deg, #7a7f86 0%, #c8c9cc 55%, #3b4c6a 100%); }

  .site-footer { position: absolute; left: 0; top: 1110px; width: 904px; height: 90px; background: var(--footer); color: var(--white); }
  .footer-col { position: absolute; top: 18px; }
  .footer-col h4 { font-size: 11px; font-weight: 500; letter-spacing: .5px; margin-bottom: 10px; }
  .footer-col p { font-size: 8.5px; line-height: 15px; }
  .footer-social { display: flex; gap: 8px; }
  .footer-social span { width: 17px; height: 17px; border-radius: 50%; background: var(--white); }
  .footer-brand { position: absolute; left: 690px; top: 26px; font-family: "Questrial", sans-serif; font-size: 24px; }
  .copyright { position: absolute; left: 686px; top: 68px; font-size: 8.5px; }
</style>
</head>
<body>

<header class="site-header">
  <div class="brand"><span class="brand-dot"></span>Byte Vale</div>
  <div class="top-contact">Call Us Today! 01632 960 418|sales@byte-vale.com</div>
  <div class="social"><span></span><span></span><span></span><span></span><span></span></div>
  <nav class="main-nav">
    <a class="active" href="#">Home</a><span class="sep">|</span>
    <a href="#">About us</a><span class="sep">|</span>
    <a href="#">Laptops</a><span class="sep">|</span>
    <a href="#">Pcs</a><span class="sep">|</span>
    <a href="#">Store</a><span class="sep">|</span>
    <a href="#">Contact us</a><span class="sep">|</span>
  </nav>
  <div class="search-btn">
    <svg width="24" height="24" viewBox="0 0 24 24"><circle cx="11" cy="11" r="4" fill="none" stroke="#1c6a86" stroke-width="1.8"/><line x1="14" y1="14" x2="17" y2="17" stroke="#1c6a86" stroke-width="1.8"/></svg>
  </div>
</header>

<section class="hero">
  <div class="hero-photo" role="img" aria-label="Desktop monitor on a desk beside a hand using a wired mouse"></div>
  <h1 class="hero-title">Repair Expertise</h1>
  <p class="hero-sub">Lorem Ipsum is simply dummy text of the printing and typesetting industry. Lorem Ipsum</p>
</section>

<section class="welcome-band">
  <span class="lead">WELCOME. HOW CAN WE HELP?</span>
  <span class="call">Call Us Today! 01632 960 418</span>
</section>

<section class="services">
  <h2 class="section-title">WHAT WE OFFER!</h2>
  <p class="section-sub">Creating solutions that work.</p>
  <div class="section-rule"></div>

  <div class="service svc-red">
    <div class="service-ring"><div class="service-disc">
      <svg width="28" height="24" viewBox="0 0 28 24"><rect x="2" y="2" width="24" height="15" rx="1" fill="none" stroke="#fff" stroke-width="2"/><rect x="10" y="19" width="8" height="3" fill="#fff"/></svg>
    </div></div>
    <h3>DC JACK REPAIR</h3>
    <p>Leading supplier of public access and internet billing systems.</p>
  </div>

  <div class="service svc-orange">
    <div class="service-ring"><div class="service-disc">
      <svg width="26" height="24" viewBox="0 0 26 24"><rect x="2" y="3" width="22" height="18" rx="2" fill="none" stroke="#fff" stroke-width="2"/><line x1="2" y1="8" x2="24" y2="8" stroke="#fff" stroke-width="2"/></svg>
    </div></div>
    <h3>SYSTEM INSTALLATION</h3>
    <p>Turn you standard TV into a full guest information system and point of sale</p>
  </div>

  <div class="service svc-cyan">
    <div class="service-ring"><div class="service-disc">
      <svg width="30" height="26" viewBox="0 0 30 26"><rect x="3" y="2" width="24" height="16" rx="1" fill="none" stroke="#fff" stroke-width="2"/><rect x="1" y="19" width="28" height="3" fill="#fff"/><rect x="11" y="9" width="8" height="6" fill="#fff"/><path d="M12.5 9 V7 a2.5 2.5 0 0 1 5 0 V9" fill="none" stroke="#fff" stroke-width="1.5"/></svg>
    </div></div>
    <h3>VIRUS REMOVAL</h3>
    <p>Our guest acceess solutions have been built with the guest in mind and are easy to use</p>
  </div>

  <div class="service svc-navy">
    <div class="service-ring"><div class="service-disc">
      <svg width="30" height="24" viewBox="0 0 30 24"><rect x="2" y="2" width="26" height="17" rx="1" fill="none" stroke="#fff" stroke-width="2"/><path d="M9 8 L12 10.5 L9 13 M21 8 L18 10.5 L21 13" fill="none" stroke="#fff" stroke-width="1.6"/><rect x="11" y="20" width="8" height="2" fill="#fff"/></svg>
    </div></div>
    <h3>SCREEN REPAIR</h3>
    <p>Get more out of your existing Wi-Fi with our social plug-ins to gain valuable insight into users</p>
  </div>
</section>

<section class="report-band">
  <h2>REPORT ONLINE</h2>
  <p>We have an online form ready and waiting for you to send your problem through. We will get back to you as soon as possible to get it fixed!</p>
  <a class="report-btn">SUBMIT YOUR COMPLAINT NOW</a>
</section>

<section class="about">
  <h2>About us</h2>
  <p>Byte Vale are a highly professional local repair specialists based in Exmere, Devon. We have been trading since 2004, with over 28 years experience.Here at Byte Vale we offer a full range of repair, service &amp; upgrade options to suit every make and model of PC system both old &amp; new.Our specialist engineers are fully trained in all aspects of PC maintenance, and work is always carried out to the highest standards.</p>
  <div class="about-photo" role="img" aria-label="Shop interior with shelves of computer parts and a service counter"></div>
</section>

<footer class="site-footer">
  <div class="footer-col" style="left:66px">
    <h4>LOCATION</h4>
    <p>14 Larchmont Way,Exmere,<br>Devon, EX9 2QT<br>01632 960 418 Emailsales@byte-vale.com</p>
  </div>
  <div class="footer-col" style="left:299px">
    <h4>CONTACT US</h4>
    <p>Phone: 555-014-2273<br>Email: hello@byte-vale.com</p>
  </div>
  <div class="footer-col" style="left:494px">
    <h4>FOLLOW US</h4>
    <div class="footer-social"><span></span><span></span><span></span><span></span></div>
  </div>
  <div class="footer-brand">Byte Vale</div>
  <div class="copyright">Copyright 2016 © BYTE-VALE</div>
</footer>

</body>
</html>
```